Capability Statement Document/Flyer

Take the existing words from the capability statement document (attached) and design a unique folder/flyer document for professional use. Maybe something like a trifold or bifold style. Use approved colours and logo as per the attached files.
Our company designs and builds small onshore gas processing plants.

Sick

```html
<!DOCTYPE html>
<html lang="en">
<head>
<meta charset="utf-8">
<title>Tarnvale Capability Statement</title>
<link href="https://fonts.googleapis.com/css2?family=Montserrat:wght@400;500;600;700;800&display=swap" rel="stylesheet">
<style>
:root{
  --green:#0a7a63;
  --green-dark:#06604e;
  --green-soft:#dfe8db;
  --grey-bg:#d6d6d6;
  --paper:#efefef;
  --ink:#3a3a3a;
  --white:#ffffff;
}
*{box-sizing:border-box;margin:0;padding:0}
html,body{width:696px;height:1200px;overflow:hidden}
body{background:var(--grey-bg);font-family:'Montserrat',sans-serif;color:var(--ink);position:relative}
.spread{position:absolute;left:12px;width:672px;height:475px;display:flex;overflow:hidden;box-shadow:0 4px 14px rgba(0,0,0,.18)}
.spread--outside{top:95px}
.spread--inside{top:630px}
.panel{position:relative;width:224px;height:100%;overflow:hidden}
.photo{position:absolute}
/* outside left */
.panel--benefits{background:var(--green)}
.info-box{position:absolute;left:10px;width:204px;border:1.5px solid var(--white);border-radius:8px;padding:10px 10px 4px;color:var(--white)}
.info-box h3{font-size:10px;font-weight:800;margin-bottom:7px}
.tick-list{list-style:none}
.tick-list li{position:relative;padding-left:14px;font-size:6.8px;line-height:1.3;margin-bottom:8px}
.tick-list li::before{content:"";position:absolute;left:0;top:1px;width:8px;height:8px;border-radius:50%;background:var(--white)}
.tick-list li::after{content:"";position:absolute;left:2.3px;top:2.8px;width:3.2px;height:1.8px;border-left:1.2px solid var(--green);border-bottom:1.2px solid var(--green);transform:rotate(-45deg)}
.photo--engineer{left:0;top:330px;width:224px;height:145px;background:linear-gradient(180deg,#8aa3c4 0%,#c9a28a 45%,#5b4a48 75%,#2e2a2c 100%)}
/* outside middle */
.panel--roles{background:var(--paper)}
.roles-top{position:absolute;left:0;top:0;width:224px;height:330px;background:var(--green);border-bottom-right-radius:36px}
.roles-top h3{position:absolute;left:14px;top:16px;font-size:9.5px;font-weight:800;color:var(--white)}
.roles-table{position:absolute;left:14px;top:46px;width:200px;color:var(--white)}
.roles-head{display:flex;background:var(--green-dark);font-size:6.8px;font-weight:700;height:15px;align-items:center}
.roles-head span:first-child{width:84px;text-align:center;border-right:1px solid rgba(255,255,255,.3)}
.roles-head span:last-child{padding-left:7px}
.roles-row{display:flex;align-items:center;height:30px;border-bottom:1px solid rgba(255,255,255,.25);font-size:7.5px;line-height:1.15}
.roles-row:last-child{border-bottom:none}
.role-icon{width:22px;height:22px;border-radius:50%;background:var(--white);margin-right:6px;flex:none;display:flex;align-items:center;justify-content:center}
.roles-owner-cell{display:flex;align-items:center;width:84px;height:100%;border-right:1px solid rgba(255,255,255,.25)}
.role-service{padding-left:7px}
.brand-word{position:absolute;left:0;width:224px;top:252px;text-align:center;color:var(--white);font-size:26px;font-weight:700;letter-spacing:1px}
.contact{position:absolute;left:24px;top:357px}
.contact h2{font-size:16px;font-weight:800;color:var(--green);margin-bottom:8px}
.contact p{display:flex;align-items:center;font-size:9.5px;font-weight:600;color:var(--green);margin-bottom:6px}
.contact svg{margin-right:7px}
.bottom-band{position:absolute;left:0;bottom:0;width:224px;height:6px;background:var(--green)}
/* outside right */
.panel--cover{background:linear-gradient(180deg,#f2f2f2,#dadada)}
.cover-word{position:absolute;left:0;width:224px;top:16px;text-align:center;color:var(--green);font-size:30px;font-weight:700;letter-spacing:1px}
.photo--plant{left:0;top:64px;width:224px;height:240px;background:linear-gradient(180deg,#a9b8c9 0%,#d4d7db 35%,#8e8f8e 65%,#a78a5e 100%)}
.cover-card{position:absolute;left:0;top:285px;width:224px;height:190px;background:linear-gradient(180deg,#ededed,#d9d9d9);border-top-left-radius:60px}
.cover-card h1{position:absolute;left:0;width:224px;top:20px;text-align:center;font-size:23px;line-height:1.05;font-weight:800;color:var(--green)}
.cover-card .tagline{position:absolute;left:0;width:224px;top:74px;text-align:center;font-size:9.5px;font-weight:700;color:var(--green);line-height:1.35}
.cover-band{position:absolute;left:0;bottom:0}
.cover-url{position:absolute;left:28px;bottom:11px;font-size:8px;font-weight:700;color:var(--white)}
/* inside left */
.panel--about{background:var(--paper)}
.bar-title{position:absolute;height:18px;background:var(--green);color:var(--white);font-size:10px;font-weight:800;display:flex;align-items:center;justify-content:center}
.panel--about .bar-title{left:12px;top:20px;width:196px}
.about-body{position:absolute;left:22px;top:46px;width:190px;font-size:7px;line-height:1.28}
.vision{margin:9px -7px 9px -7px;background:var(--green-soft);border-radius:6px;padding:7px 8px}
.vision strong{display:block;color:var(--green);font-size:8.5px;font-weight:700;margin-bottom:3px}
.vision em{font-size:7.5px;font-weight:600}
.sub-head{color:var(--green);font-size:8.5px;font-weight:700;margin-bottom:3px}
.steps{display:flex;align-items:center;justify-content:space-between;border:1.5px solid var(--green);border-radius:6px;padding:5px 6px;margin:9px -7px 9px -7px}
.step{display:flex;align-items:center;font-size:4.8px;line-height:1.2}
.step b{width:15px;height:15px;border-radius:50%;background:var(--green);color:var(--white);display:flex;align-items:center;justify-content:center;font-size:8px;margin-right:4px;flex:none}
.objective-head{font-size:9px;font-weight:600;margin-bottom:2px}
.objective-head span{color:var(--green)}
.photo--site{left:0;top:382px;width:448px;height:93px;background:linear-gradient(180deg,#b9c6cf 0%,#9aa7a4 40%,#6f7b72 70%,#53605a 100%);z-index:2}
/* inside middle */
.panel--services{background:#f4f4f4}
.panel--services .bar-title{left:14px;top:20px;width:196px}
.services{position:absolute;left:14px;top:48px;width:202px;display:grid;grid-template-columns:1fr 1fr;column-gap:6px;row-gap:9px}
.service{display:flex;align-items:flex-start}
.service svg{flex:none;margin-right:4px;margin-top:1px}
.service h4{font-size:7.4px;font-weight:600;line-height:1.1;margin-bottom:2px;color:#2a2a2a}
.service p{font-size:5px;line-height:1.25}
/* inside right */
.panel--team{background:var(--green)}
.photo--refinery{left:0;top:0;width:224px;height:112px;background:linear-gradient(180deg,#d7e3ef 0%,#c3ccd3 45%,#6f8d5f 75%,#3f6a3a 100%)}
.team-title{position:absolute;left:18px;top:126px;font-size:10px;font-weight:800;color:var(--white)}
.person{position:absolute;left:18px;display:flex;align-items:flex-start;color:var(--white)}
.portrait{width:50px;height:54px;border:1.5px solid var(--white);border-radius:3px;background:linear-gradient(160deg,#d9dde2,#8c949c);flex:none;margin-right:10px}
.person h4{font-size:9px;font-weight:700;line-height:1.1}
.person .role{font-size:7.5px;font-weight:700;margin-bottom:4px}
.person p{font-size:6.3px;line-height:1.3}
</style>
</head>
<body>

<section class="spread spread--outside">
  <div class="panel panel--benefits">
    <div class="info-box" style="top:16px">
      <h3>PDP BENEFITS:</h3>
      <ul class="tick-list">
        <li>Provides owners with access to experienced project delivery capability</li>
        <li>Improved project controls and governance</li>
        <li>Greater flexibility than traditional EPC delivery</li>
        <li>Enhanced visibility and management of cost, schedule and risk</li>
        <li>Scalable resources aligned with project phases</li>
      </ul>
    </div>
    <div class="info-box" style="top:170px">
      <h3>PDP CHALLENGES:</h3>
      <ul class="tick-list">
        <li>Owner retains significant delivery risk</li>
        <li>Requires clear governance and decision-making processes</li>
        <li>Multiple contractor interfaces require strong coordination</li>
        <li>Success depends on collaborative Owner-PDP relationship</li>
      </ul>
    </div>
    <div class="photo photo--engineer" role="img" aria-label="Engineer in hard hat and safety vest using a tablet beside a refinery at dusk"></div>
  </div>

  <div class="panel panel--roles">
    <div class="roles-top">
      <h3>PDP ROLES &amp; RESPONSIBILITIES</h3>
      <div class="roles-table">
        <div class="roles-head"><span>OWNER</span><span>TARNVALE SERVICE</span></div>
        <div class="roles-row"><div class="roles-owner-cell"><span class="role-icon"><svg width="12" height="12" viewBox="0 0 12 12"><circle cx="6" cy="6" r="4.5" fill="none" stroke="#0a7a63" stroke-width="1.2"/><circle cx="6" cy="6" r="1.6" fill="#0a7a63"/></svg></span>Sets Project Objectives</div><div class="role-service">Develops Delivery Plans</div></div>
        <div class="roles-row"><div class="roles-owner-cell"><span class="role-icon"><svg width="12" height="12" viewBox="0 0 12 12"><rect x="2" y="1.5" width="8" height="9" fill="none" stroke="#0a7a63" stroke-width="1.2"/><path d="M4 4.5h4M4 7h4" stroke="#0a7a63" stroke-width="1"/></svg></span>Develops Delivery Plans</div><div class="role-service">Provides Recommendations</div></div>
        <div class="roles-row"><div class="roles-owner-cell"><span class="role-icon"><svg width="12" height="12" viewBox="0 0 12 12"><rect x="2" y="1.5" width="8" height="9" fill="none" stroke="#0a7a63" stroke-width="1.2"/><path d="M3.5 6l1.5 1.5 3-3" fill="none" stroke="#0a7a63" stroke-width="1.1"/></svg></span>Holds Project Risk</div><div class="role-service">Identifies and Manages Risks</div></div>
        <div class="roles-row"><div class="roles-owner-cell"><span class="role-icon"><svg width="12" height="12" viewBox="0 0 12 12"><circle cx="5.5" cy="5.5" r="3.5" fill="none" stroke="#0a7a63" stroke-width="1.2"/><path d="M8 8l2.5 2.5" stroke="#0a7a63" stroke-width="1.3"/></svg></span>Awards Contracts</div><div class="role-service">Manages Contractor Interfaces</div></div>
        <div class="roles-row"><div class="roles-owner-cell"><span class="role-icon"><svg width="12" height="12" viewBox="0 0 12 12"><rect x="2" y="1.5" width="8" height="9" rx="1" fill="none" stroke="#0a7a63" stroke-width="1.2"/><path d="M4 4h4M4 6h4M4 8h2" stroke="#0a7a63" stroke-width="1"/></svg></span>Sets Project Objectives</div><div class="role-service">Monitors Cost and Schedule Performance</div></div>
      </div>
      <div class="brand-word">TARNVALE</div>
    </div>
    <div class="contact">
      <h2>GET IN TOUCH</h2>
      <p><svg width="9" height="9" viewBox="0 0 10 10"><circle cx="5" cy="5" r="5" fill="#0a7a63"/><path d="M3.3 2.8c.3 1.8 1.5 3.3 3.6 4.1l.6-.9-1-.7-.5.5c-.8-.4-1.3-1-1.6-1.7l.5-.5-.7-1z" fill="#fff"/></svg>555-010-2040</p>
      <p><svg width="9" height="9" viewBox="0 0 10 10"><circle cx="5" cy="5" r="5" fill="#0a7a63"/><circle cx="5" cy="5" r="3" fill="none" stroke="#fff" stroke-width=".7"/><path d="M2 5h6M5 2v6" stroke="#fff" stroke-width=".6"/></svg>www.tarnvale.com.au</p>
      <p><svg width="9" height="9" viewBox="0 0 10 10"><circle cx="5" cy="5" r="5" fill="#0a7a63"/><rect x="2.5" y="3.2" width="5" height="3.6" fill="none" stroke="#fff" stroke-width=".7"/><path d="M2.5 3.2L5 5.2l2.5-2" fill="none" stroke="#fff" stroke-width=".7"/></svg>directors@tarnvale.com.au</p>
    </div>
    <div class="bottom-band"></div>
  </div>

  <div class="panel panel--cover">
    <div class="cover-word">TARNVALE</div>
    <div class="photo photo--plant" role="img" aria-label="Onshore gas processing plant with silver pipework under a pale sky"></div>
    <div class="cover-card">
      <h1>CAPABILITY<br>STATEMENT</h1>
      <p class="tagline">Simplify Project Execution,<br>Streamline Operations</p>
      <svg class="cover-band" width="224" height="42" viewBox="0 0 224 42"><path d="M0 6 C90 6 150 6 172 4 L172 42 L0 42Z" fill="#0a7a63"/><path d="M150 42 C175 30 195 6 224 4 L224 42Z" fill="#b9b9b9"/></svg>
      <span class="cover-url">www.tarnvale.com.au</span>
    </div>
  </div>
</section>

<section class="spread spread--inside">
  <div class="photo photo--site" role="img" aria-label="Aerial view of a large gas processing facility beside a coastline"></div>

  <div class="panel panel--about">
    <div class="bar-title">WHO ARE TARNVALE?</div>
    <div class="about-body">
      <p>Tarnvale are a highly experienced team of Executive, Project, Construction, Commissioning and Operations specialists who combine deep technical knowledge with proven leadership to deliver unique Project Delivery Partner services to organisations in Australia.</p>
      <div class="vision"><strong>Our vision is straightforward:</strong><em>Simplify Project Execution, Streamline Operations.</em></div>
      <p class="sub-head">What is a Project Delivery Partner?</p>
      <p>A Project Delivery Partner (PDP) provides integrated project management along with technical, commercial and delivery support services to help an organisation successfully deliver a project. The PDP acts as the owner's team while the owner retains accountability and key decision-making authority.</p>
      <div class="steps">
        <div class="step"><b>1</b>Owner<br>controls the<br>project</div>
        <div class="step"><b>2</b>PDP enables<br>delivery &amp;<br>provides<br>assurance</div>
        <div class="step"><b>3</b>Contractors<br>execute<br>the work</div>
      </div>
      <p class="objective-head"><span>PDP</span> Objective:</p>
      <p>Deliver the project safely, on schedule, within budget and ready for operations; providing owner capability throughout the project lifecycle.</p>
    </div>
  </div>

  <div class="panel panel--services">
    <div class="bar-title">PDP SERVICES:</div>
    <div class="services">
      <div class="service"><svg width="13" height="13" viewBox="0 0 14 14"><circle cx="7" cy="7" r="5" fill="none" stroke="#0a7a63" stroke-width="1.1" stroke-dasharray="2 1"/><circle cx="7" cy="7" r="2" fill="none" stroke="#0a7a63"/></svg><div><h4>Project Management</h4><p>Planning, Reporting &amp; Delivery Leadership from Concept to Completion</p></div></div>
      <div class="service"><svg width="13" height="13" viewBox="0 0 14 14"><path d="M7 1.5L12.5 12h-11z" fill="none" stroke="#0a7a63" stroke-width="1.1"/><path d="M7 5.5v3M7 10v.5" stroke="#0a7a63" stroke-width="1.1"/></svg><div><h4>Risk Management</h4><p>Risk Register, Identification, Mitigation &amp; Reporting</p></div></div>
      <div class="service"><svg width="13" height="13" viewBox="0 0 14 14"><circle cx="7" cy="5" r="2.5" fill="none" stroke="#0a7a63" stroke-width="1.1"/><path d="M2.5 13c0-3 2-4.5 4.5-4.5s4.5 1.5 4.5 4.5" fill="none" stroke="#0a7a63" stroke-width="1.1"/></svg><div><h4>Engineering</h4><p>Concept Selection, Design Coordination, Technical Assurance &amp; Value Engineering</p></div></div>
      <div class="service"><svg width="13" height="13" viewBox="0 0 14 14"><path d="M1.5 5L7 2l5.5 3zM2.5 12.5h9M3.5 6v5.5M7 6v5.5M10.5 6v5.5" fill="none" stroke="#0a7a63" stroke-width="1.1"/></svg><div><h4>Governance</h4><p>Framework, Stage Gates, Change control, Reporting &amp; Decision Support</p></div></div>
      <div class="service"><svg width="13" height="13" viewBox="0 0 14 14"><rect x="2" y="4" width="10" height="8" fill="none" stroke="#0a7a63" stroke-width="1.1"/><path d="M5 4V2.5h4V4M4 7h6M4 9.5h4" stroke="#0a7a63" stroke-width="1"/></svg><div><h4>Procurement</h4><p>Contracting Strategy, Tender Process &amp; Supplier/Contractor Management</p></div></div>
      <div class="service"><svg width="13" height="13" viewBox="0 0 14 14"><path d="M2 12.5h10M3.5 12.5V4h3v8.5M8.5 12.5V7h2.5v5.5M3.5 2h8" fill="none" stroke="#0a7a63" stroke-width="1.1"/></svg><div><h4>Construction</h4><p>Management &amp; Coordination of Contractor Execution Teams</p></div></div>
      <div class="service"><svg width="13" height="13" viewBox="0 0 14 14"><rect x="2.5" y="1.5" width="9" height="11" fill="none" stroke="#0a7a63" stroke-width="1.1"/><path d="M4.5 7l1.8 1.8 3.2-3.3" fill="none" stroke="#0a7a63" stroke-width="1.1"/></svg><div><h4>Approvals</h4><p>Land Access, Regulator Engagement, Safety Case, Permits &amp; Licenses</p></div></div>
      <div class="service"><svg width="13" height="13" viewBox="0 0 14 14"><rect x="2" y="2" width="7" height="9" fill="none" stroke="#0a7a63" stroke-width="1.1"/><circle cx="10" cy="10" r="2.5" fill="none" stroke="#0a7a63" stroke-width="1.1"/><path d="M4 5h3M4 7.5h3" stroke="#0a7a63" stroke-width="1"/></svg><div><h4>Commissioning &amp; Start-up</h4><p>Lead Commissioning &amp; Start-up, Completions System, Bring the Facility to Steady-State</p></div></div>
      <div class="service"><svg width="13" height="13" viewBox="0 0 14 14"><circle cx="7" cy="7" r="5" fill="none" stroke="#0a7a63" stroke-width="1.1"/><path d="M7 4v6M5.5 5.3h2.5a1 1 0 010 2H6a1 1 0 000 2h2.5" fill="none" stroke="#0a7a63" stroke-width="1"/></svg><div><h4>Cost Control</h4><p>Budget Development, Forecasting &amp; Management</p></div></div>
      <div class="service"><svg width="13" height="13" viewBox="0 0 14 14"><circle cx="7" cy="7" r="5" fill="none" stroke="#0a7a63" stroke-width="1.1"/><circle cx="7" cy="7" r="2" fill="none" stroke="#0a7a63" stroke-width="1.1"/></svg><div><h4>Operations Readiness</h4><p>People &amp; Organisation, Process &amp; Procedures, Systems &amp; Technology</p></div></div>
      <div class="service"><svg width="13" height="13" viewBox="0 0 14 14"><rect x="1.5" y="2.5" width="11" height="10" rx="1" fill="none" stroke="#0a7a63" stroke-width="1.1"/><path d="M1.5 5.5h11M4 1.5v2M10 1.5v2" stroke="#0a7a63" stroke-width="1.1"/></svg><div><h4>Scheduling</h4><p>Master Schedule Development, WBS, Resource Allocation, Monitoring &amp; Updating</p></div></div>
      <div class="service"><svg width="13" height="13" viewBox="0 0 14 14"><path d="M2 12L8 6M9.5 2.5a2.5 2.5 0 102 2l-1.5.5-1-1zM2.5 2.5l9 9" fill="none" stroke="#0a7a63" stroke-width="1.1"/></svg><div><h4>Operations &amp; Maintenance</h4><p>Monitor &amp; Operate Asset, Minimize Downtime, Lowest Possible OPEX for Owner</p></div></div>
    </div>
  </div>

  <div class="panel panel--team">
    <div class="photo photo--refinery" role="img" aria-label="Refinery towers rising above green trees"></div>
    <h3 class="team-title">KEY TARNVALE PERSONNEL</h3>
    <div class="person" style="top:150px"><div class="portrait" role="img" aria-label="Portrait placeholder for Liam Hartley"></div><div><h4>Liam Hartley</h4><div class="role">Executive Director</div><p>35yrs Exp:<br>Brenmoor, Talloway Energy, KTVR,<br>Quillmark Energy</p></div></div>
    <div class="person" style="top:230px"><div class="portrait" role="img" aria-label="Portrait placeholder for Duncan Rourke"></div><div><h4>Duncan Rourke</h4><div class="role">Technical Director</div><p>39yrs Exp:<br>Brenmoor, Talloway Energy, Dunmarra<br>Petroleum Co, Kestrow Petroleum,<br>Oskerline Gas Group, QVN, KTVR</p></div></div>
    <div class="person" style="top:312px"><div class="portrait" role="img" aria-label="Portrait placeholder for Martin Ashby"></div><div><h4>Martin Ashby</h4><div class="role">Commercial Director</div><p>40yrs Exp:<br>Calvanor, Tavrin, Kestrow Petroleum,<br>KTVR, Quillmark Energy</p></div></div>
    <div class="person" style="top:394px"><div class="portrait" role="img" aria-label="Portrait placeholder for Owen Tarrant"></div><div><h4>Owen Tarrant</h4><div class="role">Operations Director</div><p>27yrs Exp:<br>Kestrow Petroleum, Oskerline Gas Group,<br>QVN, KTVR, Quillmark Energy</p></div></div>
  </div>
</section>

</body>
</html>
```